Glow Up by Lakeside 21 day Challenge

We are having a Glow Up by Lakeside Challenge at our fitness studio. We need a poster design using the template attached as a reference. I have also included our Bromalux logo to put on the poster. Please DO NOT use the graphics in the flyer as we are expecting something much better :-)

-Size needed 11x17 with bleeding for printing

-We need this made in Photoshop (CS3 friendly) or at least delivered in PS as we might change some text or re-arrange the design later on.

-We need this in layers.

```html
<!DOCTYPE html>
<html lang="en">
<head>
<meta charset="utf-8">
<title>Glow Up by Lakeside Challenge – Bromalux</title>
<link rel="stylesheet" href="https://fonts.googleapis.com/css2?family=Anton&family=Oswald:wght@500;700&family=Roboto+Condensed:ital,wght@0,400;0,700;1,700&display=swap">
<style>
  :root {
    --ink: #0b0b0b;
    --red: #d7141b;
    --red-deep: #8e0a0e;
    --white: #ffffff;
    --grey: #d6d6d6;
    --skin: #6b4a3c;
  }
  * { margin: 0; padding: 0; box-sizing: border-box; }
  html, body { width: 811px; height: 1200px; overflow: hidden; background: var(--ink); }
  .poster {
    position: relative; width: 811px; height: 1200px; overflow: hidden;
    background: var(--ink); font-family: "Roboto Condensed", sans-serif; color: var(--white);
  }
  .hero-photo {
    position: absolute; left: 0; top: 0; width: 811px; height: 1118px;
    background:
      radial-gradient(ellipse 200px 360px at 470px 330px, var(--skin) 0%, #3a2620 45%, transparent 75%),
      radial-gradient(ellipse 150px 110px at 200px 440px, #4a3a36 0%, transparent 70%),
      radial-gradient(ellipse 150px 110px at 700px 290px, #3e3633 0%, transparent 70%),
      linear-gradient(180deg, #141010 0%, #0b0b0b 100%);
  }
  .shapes { position: absolute; left: 0; top: 0; }
  .brand {
    position: absolute; left: 190px; top: 26px; display: flex; align-items: center; gap: 14px;
    background: rgba(255,255,255,0.93); padding: 14px 28px;
  }
  .brand-mark { width: 30px; height: 30px; background: var(--red); }
  .brand-name {
    font-family: "Oswald", sans-serif; font-weight: 700; font-size: 46px; line-height: 1;
    color: var(--ink); letter-spacing: 1px; text-transform: uppercase;
  }
  .headline {
    position: absolute; right: 34px; top: 380px; text-align: right;
    font-family: "Anton", sans-serif; font-weight: 400; text-transform: uppercase; line-height: 1.02;
  }
  .headline-line { display: block; }
  .headline-top { font-size: 96px; }
  .headline-bottom { font-size: 116px; color: var(--red); }
  .headline .red { color: var(--red); }
  .headline .white { color: var(--white); }
  .promise {
    position: absolute; left: 22px; top: 700px; width: 280px;
    transform: rotate(-17deg); transform-origin: left top;
    font-weight: 700; font-style: italic;
    font-size: 30px; line-height: 1.15; text-align: center;
  }
  .promise em { color: var(--red); font-style: italic; }
  .benefits {
    position: absolute; left: 30px; top: 945px; width: 360px; list-style: none;
    transform: rotate(-17deg); transform-origin: left top;
    font-size: 16px; line-height: 1.2; font-weight: 700;
  }
  .benefits li { position: relative; padding-left: 22px; margin-bottom: 3px; }
  .benefits svg { position: absolute; left: 0; top: 3px; }
  .offer-badge {
    position: absolute; left: 600px; top: 800px; width: 180px; height: 180px; border-radius: 50%;
    background: var(--red); border: 5px solid var(--white);
    box-shadow: 0 0 0 3px var(--red-deep);
    display: flex; flex-direction: column; align-items: center; justify-content: center;
    text-align: center; transform: rotate(-8deg); font-weight: 700;
  }
  .offer-line { font-size: 18px; line-height: 1.15; }
  .offer-price { font-family: "Anton", sans-serif; font-size: 44px; line-height: 1.05; margin-top: 4px; }
  .offer-price small { font-size: 18px; vertical-align: middle; }
  .testimonial { position: absolute; left: 430px; top: 1020px; display: flex; align-items: center; gap: 12px; }
  .testimonial-photo {
    width: 62px; height: 62px; border-radius: 50%; border: 3px solid var(--white);
    background: radial-gradient(circle at 50% 40%, #c9a48c 0%, #7c8ea3 70%);
    flex: none;
  }
  .testimonial-quote { font-size: 15px; font-weight: 700; line-height: 1.2; width: 150px; }
  .testimonial-name { display: block; font-size: 10px; font-weight: 400; font-style: italic; color: var(--grey); margin-top: 3px; }
  .call-to-action {
    position: absolute; left: 0; bottom: 0; width: 811px; height: 82px; background: var(--ink);
    display: flex; flex-direction: column; justify-content: center; align-items: center;
    font-family: "Oswald", sans-serif; font-weight: 700; text-transform: uppercase; font-size: 27px; line-height: 1.15;
  }
  .cta-urgent { color: var(--red); }
  .cta-contact { color: var(--white); }
</style>
</head>
<body>
<main class="poster">
  <div class="hero-photo" role="img" aria-label="Photo of a fit woman in black sportswear holding dumbbells, dramatic dark studio lighting"></div>

  <svg class="shapes" width="811" height="1200" viewBox="0 0 811 1200" aria-hidden="true">
    <defs>
      <linearGradient id="redBand" x1="0" y1="0" x2="1" y2="1">
        <stop offset="0" stop-color="#e5161d"/>
        <stop offset="1" stop-color="#a80d12"/>
      </linearGradient>
    </defs>
    <polygon points="0,882 811,640 811,660 0,902" fill="#ffffff"/>
    <polygon points="0,902 811,660 811,1118 0,1118" fill="url(#redBand)"/>
    <rect x="0" y="1118" width="811" height="82" fill="#0b0b0b"/>
  </svg>

  <header class="brand">
    <span class="brand-mark"></span>
    <span class="brand-name">Bromalux</span>
  </header>

  <h1 class="headline">
    <span class="headline-line headline-top"><span class="red">Glow Up</span> <span class="white">By</span></span>
    <span class="headline-line headline-bottom">Lakeside</span>
  </h1>

  <p class="promise">Discover the Secret to <em>a Beach-Ready Body</em> in Just 21 Days!</p>

  <ul class="benefits">
    <li><svg width="15" height="13" viewBox="0 0 15 13"><path d="M1 7l4 4 9-10" fill="none" stroke="#fff" stroke-width="2.5"/></svg>9 total training sessions designed to incinerate fat off your midsection, thighs, and arms</li>
    <li><svg width="15" height="13" viewBox="0 0 15 13"><path d="M1 7l4 4 9-10" fill="none" stroke="#fff" stroke-width="2.5"/></svg>21 days of nutritional guidance, including delicious recipes</li>
    <li><svg width="15" height="13" viewBox="0 0 15 13"><path d="M1 7l4 4 9-10" fill="none" stroke="#fff" stroke-width="2.5"/></svg>A Success Session to map out your individual plan for success</li>
    <li><svg width="15" height="13" viewBox="0 0 15 13"><path d="M1 7l4 4 9-10" fill="none" stroke="#fff" stroke-width="2.5"/></svg>Your very own Personal Accountability Coach to ensure you get results</li>
  </ul>

  <div class="offer-badge">
    <span class="offer-line">You get all this<br>a $399 value<br>for ONLY</span>
    <span class="offer-price"><small>★</small>$99!<small>★</small></span>
  </div>

  <figure class="testimonial">
    <div class="testimonial-photo" role="img" aria-label="Portrait photo of a satisfied client"></div>
    <blockquote class="testimonial-quote">I've never been more fit in my life at age 41!
      <cite class="testimonial-name">- Dana Morell</cite>
    </blockquote>
  </figure>

  <footer class="call-to-action">
    <span class="cta-urgent">Hurry! Space is limited to only 20 participants!!!</span>
    <span class="cta-contact">Claim your spot now: website and phone number</span>
  </footer>
</main>
</body>
</html>
```